E-commerce Website - new look and feel

Link to website
http://198.51.100.42/~brontava/brontavale_ecommerce/index.php#

Home page
-Header
- -Search bar and add to cart
-Drop down - Multi layer category representation: 1st main category level in menu bar style, 2nd category to follow and 3rd category
-Banner
-Footer

-Search listing

Category page
-Product listing
-

Product detail page
-Product variation tabular view
-

Checkout page
-

404 link/product image not found
Should be fun and engaging customers

Recent search products/ preferred products for customers

all pages:
Headroom js search bar once you are lower down the page

Shrinking navbar

Target Market(s)

Telecommunication installers, electricians working on Industrial plants and projects, on the move customers that need immediate products, procurement officers buying for projects, hard to get items customers, Car hobbyists ( future market ) for some specific product like stainless steel braid(sleeve)

Industry/Entity Type

Telecommunications

Number of Pages Required

5+ page

Colors

Designer to choose colors to be used in the design.

Requirements
Must have
• - less cluttered design
• - Easy to navigate
• - more white area on all pages
• - quick orders
• - repetitive product ordering by customers menu/list
• - branding consistency, logo colours and design
Nice to have
• -modern look
• -user friendly for less technical and computer skilled customers
• -quick to navigate
• - fun text to make customer feel at ease when navigating through website
Should not have
• -too much details
• -

```html
<!DOCTYPE html>
<html lang="en">
<head>
<meta charset="utf-8">
<title>Brontavale – Home</title>
<link href="https://fonts.googleapis.com/css2?family=Michroma&family=Lato:wght@400;700&display=swap" rel="stylesheet">
<style>
:root{
  --yellow:#f2c200;
  --ink:#111111;
  --muted:#555555;
  --link:#1a8ad8;
  --band:#f4f4f4;
  --line:#d6d6d6;
  --footer:#0b0b0b;
  --white:#ffffff;
}
*{box-sizing:border-box;margin:0;padding:0}
html,body{width:1200px;height:3333px;overflow:hidden;background:var(--white)}
body{position:relative;font-family:'Lato',sans-serif;color:var(--ink);font-size:13px}
.abs{position:absolute}
.display{font-family:'Michroma',sans-serif;text-transform:uppercase;letter-spacing:0.5px}
svg{display:block}

/* top bar */
.topbar{top:0;left:0;width:1200px;height:40px;font-size:13px;color:var(--muted)}
.topbar .item{position:absolute;top:11px;display:flex;align-items:center;gap:8px}
.brand{top:62px;left:189px;display:flex;align-items:center;gap:10px}
.brand .dot{width:30px;height:30px;border-radius:50%;background:var(--yellow)}
.brand .name{font-family:'Michroma',sans-serif;font-size:15px;color:var(--ink);text-transform:uppercase}
.nav{top:68px;left:700px;display:flex;gap:28px;font-size:13px;align-items:center}

/* hero */
.hero{top:100px;left:0;width:1200px;height:645px;background:#f6f6f6}
.hero h1{position:absolute;left:191px;top:182px;font-size:22px;line-height:32px;font-weight:400;white-space:nowrap}
.btn{position:absolute;display:flex;align-items:center;justify-content:center;border:2px solid var(--ink);border-radius:4px;font-size:12px;background:var(--white)}
.hero .btn{left:191px;top:269px;width:151px;height:37px}
.hero-visual{position:absolute;left:478px;top:100px;width:722px;height:445px;border-radius:50% 0 0 50%;background:linear-gradient(110deg,#1d3fd6 0%,#2a55e6 30%,#d8232a 50%,#e63a3a 62%,#151515 80%,#2b2b2b 100%)}
.dots{position:absolute;display:flex;gap:8px}
.dots span{width:7px;height:7px;border-radius:50%;background:var(--ink)}
.dots span.on{background:var(--yellow)}

/* section titles */
.section-title{left:0;width:1200px;text-align:center;font-size:22px;font-weight:400;white-space:nowrap}
.tabs{top:852px;left:0;width:1200px;display:flex;justify-content:center;gap:22px;font-size:12px;color:var(--muted)}
.tabs .on{color:var(--yellow)}

/* product cards */
.card{position:absolute;width:195px;height:271px;border:3px solid var(--line);background:var(--white);text-align:center}
.card.active{border-color:var(--ink)}
.card .thumb{margin:18px auto 0;width:150px;height:110px;border-radius:6px}
.card .title{font-family:'Michroma',sans-serif;font-size:10px;text-transform:uppercase;margin-top:30px;line-height:14px}
.card .code{font-size:12px;color:var(--muted);margin-top:12px}
.card .spec{font-size:12px;color:var(--link)}
.card .price{font-size:12px;color:var(--muted)}
.arrow{position:absolute;width:30px;height:30px;border-radius:50%;display:flex;align-items:center;justify-content:center}
.arrow.dark{border:2px solid var(--ink);background:var(--white)}
.arrow.gold{background:var(--yellow)}

/* promo band */
.promo{top:1316px;left:0;width:1182px;height:302px;background:var(--band)}
.promo-visual{position:absolute;left:0;top:0;width:400px;height:302px;background:linear-gradient(150deg,#f06a2a 0%,#e84a1e 35%,#d9d9d9 70%,#bfbfbf 100%)}
.promo h2{position:absolute;left:418px;top:92px;font-size:19px;line-height:26px;font-weight:400;white-space:nowrap}
.promo p{position:absolute;left:418px;top:128px;width:580px;font-size:12px;line-height:15px;color:#333}
.promo .btn{left:418px;top:180px;width:149px;height:37px}

/* categories */
.cat{position:absolute;width:195px;height:257px;border:3px solid var(--line);text-align:center;background:var(--white)}
.cat .thumb{margin:14px auto 0;width:160px;height:130px;border-radius:6px}
.cat .title{font-family:'Michroma',sans-serif;font-size:10px;text-transform:uppercase;line-height:14px;height:42px;margin-top:26px;display:flex;align-items:flex-start;justify-content:center;padding:0 10px}
.cat .go{font-size:12px;color:var(--muted)}

/* testimonial */
.photo{left:298px;top:2521px;width:158px;height:158px;border-radius:50%;background:radial-gradient(circle at 50% 40%,#d9a98a 0%,#a86f4e 45%,#6a3d2a 100%)}
.quote-name{left:473px;top:2532px;font-size:16px;white-space:nowrap}
.stars{left:473px;top:2558px;color:var(--yellow);font-size:17px;letter-spacing:2px}
.quote{left:473px;top:2588px;width:450px;font-size:12px;line-height:15px;color:#333}
.readmore{left:473px;top:2636px;font-size:13px;display:flex;gap:8px;align-items:center}

/* perks */
.perk{position:absolute;top:2764px;width:254px;height:94px;border:2px solid var(--line);display:flex;align-items:center;gap:14px;padding-left:30px}
.perk .t{font-family:'Michroma',sans-serif;font-size:11px;text-transform:uppercase;white-space:nowrap}
.perk .s{font-size:11px;color:var(--muted)}

/* subscribe */
.subscribe{top:2915px;left:0;width:1200px;height:94px;background:var(--band)}
.subscribe h3{position:absolute;left:191px;top:33px;font-size:22px;font-weight:400;white-space:nowrap}
.subscribe .field{position:absolute;left:556px;top:25px;width:455px;height:42px;border:3px solid var(--ink);border-radius:21px;background:var(--white);font-size:12px;padding:11px 0 0 28px}
.subscribe .send{position:absolute;right:0;top:-3px;width:80px;height:42px;border:3px solid var(--ink);border-radius:21px;display:flex;align-items:center;justify-content:center;background:var(--white)}

/* footer */
.footer{top:3009px;left:0;width:1200px;height:324px;background:var(--footer);color:var(--white)}
.footer .fbrand{position:absolute;left:191px;top:40px;display:flex;flex-direction:column;gap:10px}
.footer .fbrand .dot{width:44px;height:44px;border-radius:50%;background:var(--yellow)}
.footer .fbrand .name{font-family:'Michroma',sans-serif;font-size:13px;text-transform:uppercase}
.footer .about{position:absolute;left:191px;top:136px;width:200px;font-size:12px;line-height:14px}
.footer .more{position:absolute;left:191px;top:220px;font-size:12px;color:var(--yellow)}
.footer h4{position:absolute;top:93px;font-family:'Michroma',sans-serif;font-weight:400;color:var(--yellow);font-size:15px;text-transform:uppercase;white-space:nowrap}
.footer ul{position:absolute;list-style:none;font-size:12px}
.footer .links li{margin-bottom:15px;display:flex;gap:18px;align-items:center}
.footer .links li::before{content:"";width:4px;height:4px;border-radius:50%;background:var(--yellow)}
.footer .contact li{display:flex;gap:10px;margin-bottom:10px;line-height:14px}
.footer .rule{position:absolute;left:191px;top:253px;width:818px;height:1px;background:#444}
.footer .copy{position:absolute;left:191px;top:266px;font-size:13px}
.footer .legal{position:absolute;right:191px;top:266px;font-size:13px}
</style>
</head>
<body>

<header>
  <div class="abs topbar">
    <div class="item" style="left:196px">
      <svg width="16" height="16" viewBox="0 0 16 16"><circle cx="8" cy="8" r="7" fill="none" stroke="#f2c200" stroke-width="1.5"/><path d="M5 4.5l1.5-.5 1 2-1 1a5 5 0 0 0 2.5 2.5l1-1 2 1-.5 1.5c-3 .5-7-3.5-6.5-6.5z" fill="#f2c200"/></svg>
      <span>1300 555 019</span>
    </div>
    <div class="item" style="left:322px">
      <svg width="16" height="16" viewBox="0 0 16 16"><circle cx="8" cy="8" r="7" fill="none" stroke="#f2c200" stroke-width="1.5"/><rect x="4" y="5.5" width="8" height="5.5" fill="none" stroke="#f2c200"/><path d="M4 5.5l4 3 4-3" fill="none" stroke="#f2c200"/></svg>
      <span>sales@coralwickparts.example</span>
    </div>
    <div class="item" style="left:867px">
      <svg width="16" height="16" viewBox="0 0 16 16"><circle cx="8" cy="8" r="7" fill="none" stroke="#f2c200" stroke-width="1.5"/><circle cx="8" cy="6.5" r="2" fill="#f2c200"/><path d="M4.5 12a3.5 3.5 0 0 1 7 0z" fill="#f2c200"/></svg>
      <span>Login</span>
    </div>
    <div class="item" style="left:933px">
      <svg width="17" height="16" viewBox="0 0 17 16"><path d="M1 2h3l2 8h8l2-6H5" fill="none" stroke="#f2c200" stroke-width="1.6"/><circle cx="7" cy="13" r="1.3" fill="#f2c200"/><circle cx="13" cy="13" r="1.3" fill="#f2c200"/></svg>
      <span>Cart ( 2 )</span>
    </div>
  </div>
  <div class="abs brand"><span class="dot"></span><span class="name">Brontavale</span></div>
  <nav class="abs nav">
    <span>Home</span>
    <span>Categories ▾</span>
    <span>About Us</span>
    <span>Contact Us</span>
    <svg width="13" height="13" viewBox="0 0 13 13"><circle cx="5.5" cy="5.5" r="4" fill="none" stroke="#111" stroke-width="1.6"/><path d="M8.5 8.5l3.5 3.5" stroke="#111" stroke-width="1.6"/></svg>
  </nav>
</header>

<section class="abs hero">
  <div class="hero-visual" role="img" aria-label="Close-up of red, blue and black single-core DC cables with exposed copper strands"></div>
  <h1 class="display">Red / Blue<br>DC Cable - Single Core</h1>
  <div class="btn">Shop Now</div>
  <div class="dots" style="left:191px;top:566px"><span class="on"></span><span></span><span></span></div>
</section>

<h2 class="abs display section-title" style="top:793px">Feature Products</h2>
<div class="abs tabs"><span class="on">All</span><span>Newest</span><span>Most Popular</span><span>Other</span></div>

<section class="featured">
  <div class="arrow dark" style="left:79px;top:1025px"><svg width="10" height="10" viewBox="0 0 10 10"><path d="M7 1L3 5l4 4" fill="none" stroke="#111" stroke-width="2"/></svg></div>
  <div class="card" style="left:191px;top:909px">
    <div class="thumb" role="img" aria-label="Black cold shrink tubes" style="background:linear-gradient(135deg,#f2f2f2,#2a2a2a 50%,#f2f2f2)"></div>
    <div class="title">EPDM Cold Shrink</div>
    <div class="code">CST-1</div><div class="spec">Specs</div><div class="price">$ 13.95</div>
  </div>
  <div class="card" style="left:398px;top:909px">
    <div class="thumb" role="img" aria-label="Coil of black flexible conduit" style="background:radial-gradient(circle,#f4f4f4 20%,#333 40%,#222 60%,#f4f4f4 72%)"></div>
    <div class="title">Black Nylon<br>Flexible Conduit</div>
    <div class="code">BNC12</div><div class="spec">Specs</div><div class="price">$ 2.5</div>
  </div>
  <div class="card active" style="left:604px;top:909px">
    <div class="thumb" role="img" aria-label="Reel of red and blue twin cable" style="width:90px;height:90px;border-radius:50%;background:radial-gradient(circle,#c8c8c8 15%,#7a3fb0 30%,#5a4ad0 60%,#9a9a9a 70%,#fff 72%)"></div>
    <div class="title" style="margin-top:18px">Red / Blue<br>DC Cable - Twin</div>
    <div class="code" style="margin-top:4px">CAB RB1.5</div><div class="spec">Specs</div><div class="price">$ 1.9</div>
    <svg style="margin:6px auto 0" width="17" height="16" viewBox="0 0 17 16"><path d="M1 2h3l2 8h8l2-6H5z" fill="#111"/><circle cx="7" cy="13" r="1.3" fill="#111"/><circle cx="13" cy="13" r="1.3" fill="#111"/></svg>
  </div>
  <div class="card" style="left:815px;top:909px">
    <div class="thumb" role="img" aria-label="Row of white modular circuit breakers" style="background:linear-gradient(180deg,#e9e9e9,#cfcfcf 50%,#9aa39a)"></div>
    <div class="title">Volterra<br>Circuit Breakers</div>
    <div class="code">SCH10</div><div class="spec">Specs</div><div class="price">$ 12</div>
  </div>
  <div class="arrow gold" style="left:1091px;top:1025px"><svg width="10" height="10" viewBox="0 0 10 10"><path d="M3 1l4 4-4 4" fill="none" stroke="#fff" stroke-width="2"/></svg></div>
  <div class="btn" style="left:524px;top:1229px;width:147px;height:36px">View All</div>
</section>

<section class="abs promo">
  <div class="promo-visual" role="img" aria-label="Cable cutters, screwdrivers and stripped electrical cable"></div>
  <h2 class="display">Coralwick Components Products</h2>
  <p>Free Freight On Orders Over $150 Excluding GST (VIC, NSW, QLD, SA) Free Freight On Orders Over $250 Excluding GST (WA, NT)</p>
  <div class="btn">Shop Now</div>
</section>

<h2 class="abs display section-title" style="top:1687px">Product Categories</h2>
<section class="categories">
  <div class="cat" style="left:191px;top:1756px"><div class="thumb" role="img" aria-label="Stainless steel cable ties" style="background:linear-gradient(135deg,#fafafa,#b9b9b9,#f2f2f2)"></div><div class="title">Stainless Steel Cable Ties</div><div class="go">View Category</div></div>
  <div class="cat" style="left:398px;top:1756px"><div class="thumb" role="img" aria-label="Coil of black nylon conduit" style="background:radial-gradient(circle,#fff 20%,#333 40%,#222 58%,#fff 70%)"></div><div class="title">Black Nylon Flexible Conduit</div><div class="go">View Category</div></div>
  <div class="cat" style="left:604px;top:1756px"><div class="thumb" role="img" aria-label="Coloured nylon cable ties" style="background:linear-gradient(90deg,#2040d0,#f0d020,#20a040,#e02020,#f08020)"></div><div class="title">Nylon Cable Ties</div><div class="go">View Category</div></div>
  <div class="cat" style="left:815px;top:1756px"><div class="thumb" role="img" aria-label="Red earth bar insulators" style="background:radial-gradient(circle,#e02a2a 25%,#f6f6f6 55%)"></div><div class="title">Earth Bar Insulators</div><div class="go">View Category</div></div>

  <div class="cat" style="left:191px;top:2027px"><div class="thumb" role="img" aria-label="Copper and steel earth bars" style="background:linear-gradient(160deg,#f6f6f6,#9a9a9a 50%,#f6f6f6)"></div><div class="title">Earth Bars</div><div class="go">View Category</div></div>
  <div class="cat" style="left:398px;top:2027px"><div class="thumb" role="img" aria-label="Black cold shrink tubes" style="background:linear-gradient(135deg,#f6f6f6,#2a2a2a 50%,#f6f6f6)"></div><div class="title">EPDM Cold Shrink</div><div class="go">View Category</div></div>
  <div class="cat" style="left:604px;top:2027px"><div class="thumb" role="img" aria-label="Reel of green and yellow earth cable" style="background:radial-gradient(circle,#222 20%,#6fb33a 45%,#f6f6f6 65%)"></div><div class="title">Green / Yellow Earth Cable - Multistrand</div><div class="go">View Category</div></div>
  <div class="cat" style="left:815px;top:2027px"><div class="thumb" role="img" aria-label="Yellow fibre patch lead coil" style="background:radial-gradient(circle,#fff 30%,#f0d020 45%,#fff 60%)"></div><div class="title">Fiber Patch Leads Ruggedised Single Mode Duplex</div><div class="go">View Category</div></div>

  <div class="btn" style="left:524px;top:2335px;width:149px;height:38px">View All Cateories</div>
</section>

<h2 class="abs display section-title" style="top:2453px">Testimonials</h2>
<section class="testimonial">
  <div class="arrow dark" style="left:79px;top:2567px"><svg width="10" height="10" viewBox="0 0 10 10"><path d="M7 1L3 5l4 4" fill="none" stroke="#111" stroke-width="2"/></svg></div>
  <div class="abs photo" role="img" aria-label="Portrait photo of the customer"></div>
  <div class="abs display quote-name">Dorian Kessel</div>
  <div class="abs stars">★★★★★</div>
  <p class="abs quote">Lorem Ipsum is simply dummy text of the printing and typesetting industry. Lorem Ipsum has been the industry's standard dummy text ever since the 1500s.</p>
  <div class="abs readmore">READ MORE... <svg width="12" height="12" viewBox="0 0 12 12"><circle cx="6" cy="6" r="5" fill="none" stroke="#111"/><path d="M5 3.5L7.5 6 5 8.5" fill="none" stroke="#111"/></svg></div>
  <div class="arrow gold" style="left:1091px;top:2567px"><svg width="10" height="10" viewBox="0 0 10 10"><path d="M3 1l4 4-4 4" fill="none" stroke="#fff" stroke-width="2"/></svg></div>
  <div class="dots" style="left:580px;top:2706px"><span class="on"></span><span></span><span></span></div>
</section>

<section class="perks">
  <div class="perk" style="left:193px">
    <svg width="32" height="32" viewBox="0 0 32 32"><circle cx="16" cy="14" r="10" fill="none" stroke="#111" stroke-width="2"/><path d="M12 26h8" stroke="#111" stroke-width="2"/></svg>
    <div><div class="t">Free Shipping</div><div class="s">Lorem Ipsum is dummy text.</div></div>
  </div>
  <div class="perk" style="left:473px">
    <svg width="32" height="32" viewBox="0 0 32 32"><path d="M6 18v-3a10 10 0 0 1 20 0v3" fill="none" stroke="#111" stroke-width="2"/><rect x="4" y="17" width="5" height="8" rx="2" fill="#111"/><rect x="23" y="17" width="5" height="8" rx="2" fill="#111"/></svg>
    <div><div class="t">Premium Support</div><div class="s">24/7 Customer service</div></div>
  </div>
  <div class="perk" style="left:753px">
    <svg width="36" height="32" viewBox="0 0 36 32"><rect x="2" y="8" width="20" height="14" fill="none" stroke="#111" stroke-width="2"/><path d="M22 12h7l5 5v5H22z" fill="none" stroke="#111" stroke-width="2"/><circle cx="9" cy="24" r="3" fill="#fff" stroke="#111" stroke-width="2"/><circle cx="28" cy="24" r="3" fill="#fff" stroke="#111" stroke-width="2"/></svg>
    <div><div class="t">Payment Method</div><div class="s">Cash On Delivery</div></div>
  </div>
</section>

<section class="abs subscribe">
  <h3 class="display">Subscribe Us</h3>
  <div class="field">E-Mail Address
    <div class="send"><svg width="20" height="18" viewBox="0 0 20 18"><path d="M1 8L19 1l-4 16-5-6z" fill="#111"/></svg></div>
  </div>
</section>

<footer class="abs footer">
  <div class="fbrand"><span class="dot"></span><span class="name">Brontavale</span></div>
  <p class="about">Lorem Ipsum is simply dummy text of the printing and typesetting industry. Lorem Ipsum has been the industry's standard dummy text ever since the 1500s.</p>
  <div class="more">READ MORE... ›</div>

  <h4 style="left:416px">Qucik Link</h4>
  <ul class="links" style="left:430px;top:136px">
    <li>Home</li><li>Categories</li><li>About Us</li><li>Contact Us</li>
  </ul>

  <h4 style="left:609px">Contact Us</h4>
  <ul class="contact" style="left:614px;top:131px;width:200px">
    <li><span style="color:var(--yellow)">●</span><span>Victoria : 12 Kestrel Way, Alderbrook, VIC, 3899</span></li>
    <li><span style="color:var(--yellow)">●</span><span>Queensland: 7b/310 Marlow Rd, Fernhill, QLD, 4099</span></li>
    <li><span style="color:var(--yellow)">●</span><span>1300 555 019</span></li>
    <li><span style="color:var(--yellow)">●</span><span>sales@coralwickparts.example</span></li>
  </ul>

  <h4 style="left:838px">Visit Us</h4>
  <ul class="contact" style="left:843px;top:131px;width:170px">
    <li><span style="color:var(--yellow)">●</span><span>New South Wales : 4/88 Quarry Road, Ashvale Park, NSW, 2199</span></li>
  </ul>

  <div class="rule"></div>
  <div class="copy">CopyRight ©2018 Brontavale. All Right Reserve</div>
  <div class="legal">Privacy Policy - Terms &amp; Conditions</div>
</footer>

</body>
</html>
```